Business card for Clear Harbour Lending

Front (space for each) - Name, title, qualifications, mobile number, email address, website, name/logo,
Back - Business name/logo and slogan "Your first home starts here" underneath,
in small writing underneath need ABN number, CRN number, ACL number
Target Market(s)
First Home Buyers
Industry/Entity Type
Finance
Contact Information for Business Card
Requirements
Must have
- Front (space for each) - Name, title, qualifications, mobile number, email address, website, name/logo,

```html
<!DOCTYPE html>
<html lang="en">
<head>
<meta charset="utf-8">
<title>Clear Harbour Lending – Business Card</title>
<link rel="stylesheet" href="https://fonts.googleapis.com/css2?family=Montserrat:wght@400;500;600;700&display=swap">
<style>
  :root {
    --page: #2b2b2b;
    --card: #ffffff;
    --ink: #141414;
    --ink-soft: #3a3a3a;
    --teal: #0fa9a6;
    --green: #8cc63f;
    --coral: #f2665e;
    --orange: #fbb563;
    --rule: #d9d9d9;
  }
  * { box-sizing: border-box; margin: 0; padding: 0; }
  html, body { width: 1200px; height: 1015px; overflow: hidden; }
  body {
    background: var(--page);
    font-family: "Montserrat", sans-serif;
    color: var(--ink);
    display: flex;
    flex-direction: column;
    align-items: center;
    justify-content: center;
    gap: 34px;
  }
  .card {
    position: relative;
    width: 800px;
    height: 457px;
    background: var(--card);
    border-radius: 16px;
    overflow: hidden;
    box-shadow: 0 10px 30px rgba(0,0,0,.45);
  }

  /* Business name */
  .brand {
    position: absolute;
    display: flex;
    align-items: center;
    gap: 12px;
  }
  .brand-name {
    font-weight: 700;
    font-size: 30px;
    line-height: 1;
    letter-spacing: 2px;
    text-transform: uppercase;
    color: var(--ink);
    white-space: nowrap;
  }
  .brand-mark {
    width: 14px; height: 14px; border-radius: 50%;
    background: var(--coral);
  }

  /* Back */
  .card-back .brand { top: 140px; right: 60px; }
  .tagline {
    position: absolute;
    right: 0;
    top: 232px;
    width: 470px;
    height: 40px;
    border-radius: 20px 0 0 20px;
    background: linear-gradient(90deg, var(--coral), var(--orange));
    color: #fff;
    font-weight: 500;
    font-size: 16px;
    letter-spacing: 1.5px;
    text-transform: uppercase;
    display: flex;
    align-items: center;
    padding-left: 32px;
    white-space: nowrap;
  }
  .register-band {
    position: absolute;
    left: 0; right: 0; bottom: 0;
    height: 48px;
    background: linear-gradient(90deg, var(--teal), var(--green));
    display: flex;
    align-items: center;
    justify-content: space-around;
    padding: 0 40px;
    color: #fff;
    font-size: 11px;
    font-weight: 600;
    letter-spacing: 1.2px;
    text-transform: uppercase;
    white-space: nowrap;
  }
  .soft-dot {
    position: absolute;
    border-radius: 50%;
    background: linear-gradient(135deg, #fff4ea, #fdeaea);
  }

  /* Front */
  .card-front .brand { top: 60px; left: 52px; }
  .corner-sweep { position: absolute; left: 0; bottom: 0; }
  .accent-circle {
    position: absolute;
    right: -36px; top: 110px;
    width: 80px; height: 80px; border-radius: 50%;
    background: linear-gradient(135deg, var(--orange), var(--coral));
  }
  .person {
    position: absolute;
    right: 58px;
    top: 180px;
    width: 330px;
  }
  .person-name {
    font-weight: 600;
    font-size: 26px;
    letter-spacing: 1.5px;
    text-transform: uppercase;
    white-space: nowrap;
  }
  .person-title {
    margin-top: 6px;
    font-weight: 600;
    font-size: 13px;
    letter-spacing: 1px;
    text-transform: uppercase;
    color: var(--ink-soft);
  }
  .person-rule { height: 1px; background: var(--rule); margin: 16px 0 18px; }
  .contact-list { list-style: none; display: flex; flex-direction: column; gap: 12px; }
  .contact-list li {
    display: flex; align-items: center; gap: 14px;
    font-size: 13px; color: var(--ink-soft);
    white-space: nowrap;
  }
  .contact-list li:first-child { font-weight: 600; color: var(--ink); }
  .contact-list svg { width: 22px; height: 22px; flex: none; }
</style>
</head>
<body>

  <section class="card card-back" aria-label="Card back">
    <div class="soft-dot" style="width:64px;height:64px;left:470px;top:300px"></div>
    <div class="brand">
      <div class="brand-name">Clear Harbour Lending</div>
      <div class="brand-mark"></div>
    </div>
    <div class="tagline">Your first home starts here</div>
    <div class="register-band">
      <span>ABN Number: 27 604 318 952</span>
      <span>CRN Number: 509 774</span>
      <span>ACL Number: 482 116</span>
    </div>
  </section>

  <section class="card card-front" aria-label="Card front">
    <svg class="corner-sweep" width="420" height="300" viewBox="0 0 420 300" aria-hidden="true">
      <defs>
        <linearGradient id="sweep" x1="0" y1="1" x2="1" y2="0">
          <stop offset="0" stop-color="#0fa9a6"/>
          <stop offset="1" stop-color="#8cc63f"/>
        </linearGradient>
      </defs>
      <path d="M0 300 L0 120 Q220 140 420 300 Z" fill="url(#sweep)"/>
    </svg>
    <div class="accent-circle"></div>
    <div class="brand">
      <div class="brand-name">Clear Harbour Lending</div>
      <div class="brand-mark"></div>
    </div>
    <div class="person">
      <h1 class="person-name">Marcus Denholm</h1>
      <p class="person-title">Managing Director, MD</p>
      <div class="person-rule"></div>
      <ul class="contact-list">
        <li>
          <svg viewBox="0 0 24 24" aria-hidden="true"><path d="M6.6 10.8a15 15 0 0 0 6.6 6.6l2.2-2.2c.3-.3.7-.4 1-.2 1.1.4 2.3.6 3.6.6.6 0 1 .4 1 1V20c0 .6-.4 1-1 1A17 17 0 0 1 3 4c0-.6.4-1 1-1h3.5c.6 0 1 .4 1 1 0 1.3.2 2.5.6 3.6.1.3 0 .7-.2 1z" fill="#0fa9a6"/></svg>
          (208) 555-0147
        </li>
        <li>
          <svg viewBox="0 0 24 24" aria-hidden="true"><rect x="2.5" y="5.5" width="19" height="13" rx="1" fill="none" stroke="#0fa9a6" stroke-width="1.5"/><path d="M2.5 6l9.5 7 9.5-7" fill="none" stroke="#0fa9a6" stroke-width="1.5"/></svg>
          marcus@clearharbourlending.com
        </li>
        <li>
          <svg viewBox="0 0 24 24" aria-hidden="true"><circle cx="12" cy="12" r="9" fill="none" stroke="#0fa9a6" stroke-width="1.5"/><ellipse cx="12" cy="12" rx="4" ry="9" fill="none" stroke="#0fa9a6" stroke-width="1.5"/><path d="M3 12h18" stroke="#0fa9a6" stroke-width="1.5"/></svg>
          www.clearharbourlending.com
        </li>
      </ul>
    </div>
  </section>

</body>
</html>
```